lab equipment website

We need a fresh new look for a company website called tarvio. We will be using the current logo and brand colors on their current website tarvio.com. They want to keep their text and on-page SEO, but would like to reformat it to look more modern and fresh. They want to have everything be high performance with a great user experience. Their main call to action is for people to fill in a contact form so they can call them. There is some information that is purposely above the fold on the instrument pages. I will need the home page, about page and a leasing page.

```html
<!DOCTYPE html>
<html lang="en">
<head>
<meta charset="utf-8">
<title>tarvio – Lab Support Program</title>
<link href="https://fonts.googleapis.com/css2?family=Raleway:wght@500;600;700&family=Open+Sans:ital,wght@0,400;0,600;0,700;1,400&display=swap" rel="stylesheet">
<style>
:root{
  --teal:#1bb38f;
  --teal-dark:#139a7a;
  --ink:#1f3444;
  --text:#444b52;
  --muted:#6b7279;
  --footer:#1e3444;
  --white:#ffffff;
  --line:#d6dadd;
}
*{box-sizing:border-box;margin:0;padding:0}
html,body{width:1200px;height:4196px;overflow:hidden}
body{position:relative;background:var(--white);font-family:"Open Sans",Arial,sans-serif;color:var(--text)}
.abs{position:absolute}
h1,h2,h3{font-family:"Raleway",Arial,sans-serif;color:var(--ink)}
.btn{position:absolute;display:flex;align-items:center;justify-content:center;border-radius:40px;font-family:"Open Sans",Arial,sans-serif;font-weight:700;font-size:17px;letter-spacing:.5px;text-transform:uppercase;text-decoration:none}
.btn-solid{background:var(--teal);color:var(--white)}
.btn-ghost{border:3px solid var(--white);color:var(--white)}

/* hero */
.hero{position:absolute;left:0;top:0;width:1200px;height:613px;overflow:hidden;background:linear-gradient(100deg,#5d6266 0%,#8a8f93 35%,#c9cdcf 70%,#e4e6e7 100%)}
.hero-hex{position:absolute;left:0;top:0}
.brand{position:absolute;left:112px;top:34px;display:flex;align-items:center;gap:12px;color:var(--white);font-family:"Raleway",Arial,sans-serif;font-weight:700;font-size:34px}
.brand-dot{width:30px;height:30px;border-radius:50%;background:var(--teal)}
.nav{position:absolute;right:60px;top:52px;display:flex;align-items:center;gap:30px;font-weight:600;font-size:16px;color:var(--white);text-transform:uppercase}
.nav .active{position:relative;padding:8px 4px}
.nav .active::before{content:"";position:absolute;left:-8px;top:-4px;width:60px;height:40px;border:2px solid rgba(255,255,255,.8);clip-path:polygon(25% 0,75% 0,100% 50%,75% 100%,25% 100%,0 50%)}
.hero h1{position:absolute;left:112px;top:194px;color:var(--white);font-size:58px;line-height:70px;font-weight:700}
.hero .btn{left:114px;top:380px;width:204px;height:60px;font-size:16px}
.dots{position:absolute;left:112px;top:519px;display:flex;gap:6px}
.dots span{width:14px;height:14px;border-radius:50%;border:2px solid var(--white)}
.dots span.on{background:var(--white)}

/* goal */
.goal h2{position:absolute;left:0;width:1200px;top:700px;text-align:center;font-size:46px;font-weight:600}
.goal p.lead{position:absolute;left:240px;width:720px;top:780px;text-align:center;font-size:16px;line-height:32px;color:var(--muted)}
.feature{position:absolute;top:895px;width:360px;text-align:center}
.feature svg{display:block;margin:0 auto}
.feature h3{margin-top:38px;font-family:"Open Sans",Arial,sans-serif;font-weight:600;font-size:21px;line-height:31px;color:var(--ink)}
.goal .btn{left:515px;top:1247px;width:170px;height:60px}

/* split sections */
.split-media{position:absolute}
.split-copy h2{font-size:46px;font-weight:600}
.split-copy .sub{color:var(--teal);font-weight:600;font-size:19px;line-height:34px}
.split-copy p{font-size:14.5px;line-height:27px;color:var(--text)}
.who{position:absolute;left:671px;top:1548px;width:440px}
.who .sub{margin-top:18px}
.who p{margin-top:22px}
.who-btn{left:677px;top:1857px;width:170px;height:62px}
.why{position:absolute;left:106px;top:2172px;width:440px}
.why .sub{margin-top:18px}
.ticks{list-style:none;margin-top:32px}
.ticks li{position:relative;padding-left:32px;font-size:14.5px;line-height:24px;margin-bottom:21px}
.ticks li svg{position:absolute;left:0;top:3px}
.why-btn{left:112px;top:2654px;width:170px;height:62px}

/* cta band */
.cta{position:absolute;left:0;top:2845px;width:1200px;height:402px;background:var(--teal);text-align:center}
.cta h2{color:var(--white);font-size:46px;font-weight:600;margin-top:80px}
.cta p{color:var(--white);font-size:20px;line-height:37px;width:680px;margin:24px auto 0}
.cta .btn{left:500px;top:254px;width:198px;height:62px;gap:10px}

/* testimonials */
.testi h2{position:absolute;left:0;width:1200px;top:3332px;text-align:center;font-size:46px;font-weight:600}
.quote{position:absolute;left:230px;width:740px;top:3562px;text-align:center;font-style:italic;font-size:16px;line-height:32px;color:var(--muted)}
.person{position:absolute;left:0;width:1200px;top:3684px;text-align:center}
.person strong{display:block;font-family:"Open Sans",Arial,sans-serif;font-weight:700;font-size:20px;color:var(--ink);text-transform:uppercase}
.person span{display:block;margin-top:6px;color:var(--teal);font-size:14px;text-transform:uppercase}
.arrow{position:absolute;top:3589px}

/* footer */
.footer{position:absolute;left:0;top:3871px;width:1200px;height:325px;background:var(--footer);color:var(--white);text-align:center}
.socials{position:absolute;left:519px;top:61px;display:flex;gap:9px}
.socials span{width:48px;height:48px;border-radius:50%;border:2px solid var(--white)}
.contact-line{position:absolute;left:0;width:1200px;top:147px;font-size:15px;display:flex;justify-content:center;align-items:center;gap:10px}
.links{position:absolute;left:0;width:1200px;top:191px;font-size:15px;display:flex;justify-content:center;gap:18px}
.copy{position:absolute;left:0;width:1200px;top:233px;font-size:15px}
</style>
</head>
<body>

<header class="hero">
  <div class="abs" role="img" aria-label="Laboratory microscope photo" style="left:0;top:0;width:1200px;height:613px;background:linear-gradient(100deg,#5d6266 0%,#8a8f93 35%,#c9cdcf 70%,#e4e6e7 100%)"></div>
  <svg class="hero-hex" width="1200" height="613" viewBox="0 0 1200 613" aria-hidden="true">
    <polygon points="650,-120 1000,-120 1175,280 1000,680 650,680 480,280" fill="#2fd6a6" fill-opacity=".72"/>
  </svg>
  <div class="brand"><span class="brand-dot"></span>tarvio</div>
  <nav class="nav">
    <span class="active">Home</span><span>About</span><span>Leasing</span><span>FAQ</span><span>Contact</span>
    <svg width="20" height="20" viewBox="0 0 20 20"><circle cx="8" cy="8" r="6" fill="none" stroke="#fff" stroke-width="2.5"/><line x1="12.5" y1="12.5" x2="18" y2="18" stroke="#fff" stroke-width="2.5"/></svg>
  </nav>
  <h1>Your Success,<br>our Support</h1>
  <a class="btn btn-ghost">Get More Info</a>
  <div class="dots"><span class="on"></span><span></span><span></span><span></span></div>
</header>

<section class="goal">
  <h2>Our goal is simple: save labs time and money</h2>
  <p class="lead">Tarvio is a lab support program that provides scientists with comprehensive maintenance/repair coverage and operating lease solutions at an affordable price.</p>

  <div class="feature" style="left:55px">
    <svg width="212" height="184" viewBox="0 0 212 184"><polygon points="55,2 157,2 209,92 157,182 55,182 3,92" fill="none" stroke="#cfd3d6" stroke-width="2"/><circle cx="106" cy="92" r="46" fill="#d4f1e8" role="img" aria-label="Microscope icon"/></svg>
    <h3>Worry free lab equipment<br>PM/repair coverage</h3>
  </div>
  <div class="feature" style="left:420px">
    <svg width="212" height="184" viewBox="0 0 212 184"><polygon points="55,2 157,2 209,92 157,182 55,182 3,92" fill="none" stroke="#cfd3d6" stroke-width="2"/><circle cx="106" cy="92" r="46" fill="#d4f1e8" role="img" aria-label="Gears and dollar icon"/></svg>
    <h3>Cost-effective lease structures<br>and payment plans</h3>
  </div>
  <div class="feature" style="left:785px">
    <svg width="212" height="184" viewBox="0 0 212 184"><polygon points="55,2 157,2 209,92 157,182 55,182 3,92" fill="none" stroke="#cfd3d6" stroke-width="2"/><circle cx="106" cy="92" r="46" fill="#d4f1e8" role="img" aria-label="Lab clipboard icon"/></svg>
    <h3>Knowledge of the<br>laboratory</h3>
  </div>
  <a class="btn btn-solid">Learn More</a>
</section>

<section>
  <svg class="split-media" style="left:0;top:1426px" width="600" height="551" viewBox="0 0 600 551" role="img" aria-label="Gloved hand holding a blood test tube beside a stethoscope">
    <defs><linearGradient id="whoFill" x1="0" y1="0" x2="1" y2="1"><stop offset="0" stop-color="#4fb6d8"/><stop offset=".45" stop-color="#e9e9ec"/><stop offset="1" stop-color="#9aa0a6"/></linearGradient></defs>
    <polygon points="0,175 300,0 600,175 600,376 300,551 0,376" fill="url(#whoFill)"/>
  </svg>
  <div class="who split-copy">
    <h2>Who We Are</h2>
    <div class="sub">Trusted Company Offering Scientific Equipment Service Plans and Flexible Leases</div>
    <p>At Tarvio, our goal is to ensure the success of your business. Whether you are running a laboratory or other scientific facilities, we want to keep you provided with the best in cutting-edge equipment.</p>
  </div>
  <a class="btn btn-solid who-btn">Learn More</a>
</section>

<section>
  <div class="why split-copy">
    <h2>Why Choose Us</h2>
    <div class="sub">We Understand Your Needs Because We Are Scientists First</div>
    <ul class="ticks">
      <li><svg width="18" height="18" viewBox="0 0 18 18"><circle cx="9" cy="9" r="9" fill="#1bb38f"/><path d="M5 9.3l2.7 2.6L13 6.5" fill="none" stroke="#fff" stroke-width="2"/></svg>We collaborate with you directly- no middlemen</li>
      <li><svg width="18" height="18" viewBox="0 0 18 18"><circle cx="9" cy="9" r="9" fill="#1bb38f"/><path d="M5 9.3l2.7 2.6L13 6.5" fill="none" stroke="#fff" stroke-width="2"/></svg>We handle scientific equipment service, repairs, and maintenance</li>
      <li><svg width="18" height="18" viewBox="0 0 18 18"><circle cx="9" cy="9" r="9" fill="#1bb38f"/><path d="M5 9.3l2.7 2.6L13 6.5" fill="none" stroke="#fff" stroke-width="2"/></svg>We consolidate and streamline the ancillary work associated with lab equipment procurement and service</li>
      <li><svg width="18" height="18" viewBox="0 0 18 18"><circle cx="9" cy="9" r="9" fill="#1bb38f"/><path d="M5 9.3l2.7 2.6L13 6.5" fill="none" stroke="#fff" stroke-width="2"/></svg>We utilize our networks to bring you the most cost-savings possible</li>
      <li><svg width="18" height="18" viewBox="0 0 18 18"><circle cx="9" cy="9" r="9" fill="#1bb38f"/><path d="M5 9.3l2.7 2.6L13 6.5" fill="none" stroke="#fff" stroke-width="2"/></svg>We may provide tax advantages with our lease structures</li>
    </ul>
  </div>
  <a class="btn btn-solid why-btn">Learn More</a>
  <svg class="split-media" style="left:600px;top:2053px" width="600" height="627" viewBox="0 0 600 627" role="img" aria-label="Gloved hand loading a sample plate into a lab instrument">
    <defs><linearGradient id="whyFill" x1="0" y1="0" x2="1" y2="1"><stop offset="0" stop-color="#f1f2f3"/><stop offset=".5" stop-color="#3a4a66"/><stop offset="1" stop-color="#3fa6e0"/></linearGradient></defs>
    <polygon points="0,190 300,0 600,190 600,437 300,627 0,437" fill="url(#whyFill)"/>
  </svg>
</section>

<section class="cta">
  <h2>Further Questions?</h2>
  <p>Feel free to contact us if you have any questions or comments. We promise to get back to you within 24 hours.</p>
  <a class="btn btn-ghost"><svg width="18" height="14" viewBox="0 0 18 14"><rect x="0" y="0" width="18" height="14" rx="2" fill="#fff"/><path d="M1 1l8 6 8-6" fill="none" stroke="#1bb38f" stroke-width="1.6"/></svg>Contact Us</a>
</section>

<section class="testi">
  <h2>Testimonials</h2>
  <svg class="abs" style="left:542px;top:3424px" width="116" height="116" viewBox="0 0 116 116">
    <polygon points="58,2 108,30 108,86 58,114 8,86 8,30" fill="#f1f2f3"/>
    <polygon points="58,10 101,34 101,82 58,106 15,82 15,34" fill="#c9b8a6" role="img" aria-label="Portrait of the reviewer"/>
  </svg>
  <svg class="arrow" style="left:89px" width="46" height="46" viewBox="0 0 46 46"><circle cx="23" cy="23" r="21" fill="none" stroke="#3a4248" stroke-width="2"/><path d="M26 15l-8 8 8 8" fill="none" stroke="#3a4248" stroke-width="2.5"/></svg>
  <svg class="arrow" style="left:1063px" width="46" height="46" viewBox="0 0 46 46"><circle cx="23" cy="23" r="21" fill="none" stroke="#3a4248" stroke-width="2"/><path d="M20 15l8 8-8 8" fill="none" stroke="#3a4248" stroke-width="2.5"/></svg>
  <p class="quote">My time spent in the lab opened my eyes to the passion and dedication that drives scientists, as well as the frustration of a tight budget and equipment upkeep. Tarvio was created in order to help overcome these obstacles and enable scientists to focus on what they're truly passionate about: research.</p>
  <div class="person"><strong>Dana Reyes</strong><span>Lab Relations</span></div>
</section>

<footer class="footer">
  <div class="socials"><span></span><span></span><span></span></div>
  <div class="contact-line">
    <svg width="12" height="16" viewBox="0 0 12 16"><path d="M6 0a6 6 0 0 0-6 6c0 4.5 6 10 6 10s6-5.5 6-10a6 6 0 0 0-6-6z" fill="#fff"/><circle cx="6" cy="6" r="2.2" fill="#1e3444"/></svg>
    <span>48 Harbor Lane Suite 300 Oakland, CA 94607</span><span>|</span>
    <svg width="15" height="15" viewBox="0 0 15 15"><path d="M3 0l3 3-2 2c1 2 3 4 5 5l2-2 3 3-2 3C6 14 1 9 0 3z" fill="#fff"/></svg>
    <span>(510) 555-0148</span><span>|</span>
    <svg width="17" height="13" viewBox="0 0 17 13"><rect width="17" height="13" rx="2" fill="#fff"/><path d="M1 1l7.5 6L16 1" fill="none" stroke="#1e3444" stroke-width="1.5"/></svg>
    <span>info@tarvio.com</span>
  </div>
  <div class="links"><span>Help</span><span>|</span><span>FAQ</span><span>|</span><span>Support</span><span>|</span><span>Sitemap</span><span>|</span><span>Terms Of Use</span><span>|</span><span>Privacy Statement</span></div>
  <div class="copy">Tarvio © 2019 All rights reserved.</div>
</footer>

</body>
</html>
```